Expanding Wealth Training Company Needs Training Program Brochures

We are expanding our range of courses and need to have attractive designs for 3 of the new courses we are launching.
Target Audience: Financial service professionals
Nationalities: Predominantly Asian
Courses:
1. Practical Estate Planning for Sales Growth - Level 1
2. Practical Protection Planning for Business Owners - Level 1
3. Practical Financial Counselling
The corporate color for the training company (Brightvale Institute) is RED. You can go to www.brightvaleinstitute.com.sg to see the colors. The current brochures are attached but please follow the write-ups in the separately attached Word files.

Target Market(s)

Financial Service Professionals (as known as financial planners)

Industry/Entity Type

Training

Requirements
Must have
• 1. Faces of professional people are work - either in a planning situation or counseling situation. Can have a mix of Western and Asian faces.
2. Limit to 2 pages (front and back) of a single sheet.

```html
<!DOCTYPE html>
<html lang="en">
<head>
<meta charset="utf-8">
<title>Practical Financial Counselling – Course Brochure</title>
<link rel="stylesheet" href="https://fonts.googleapis.com/css2?family=Questrial&family=Montserrat:wght@500;600;700&display=swap">
<style>
:root{
  --red:#c8202f;
  --ink:#2b2b2b;
  --soft:#a9a9a9;
  --backdrop:#dedede;
  --paper:#ffffff;
}
*{margin:0;padding:0;box-sizing:border-box}
html,body{width:1200px;height:800px;overflow:hidden}
body{background:var(--backdrop);font-family:"Questrial",sans-serif;color:var(--ink);position:relative}
.page{position:absolute;background:var(--paper);overflow:hidden}
.abs{position:absolute}
h1,h2,p{font-weight:400}

/* Front cover */
.cover{left:48px;top:48px;width:490px;height:694px}
.partner{left:60px;top:160px;width:220px;text-align:center}
.partner-name{font-family:"Questrial",sans-serif;font-size:10.5px;line-height:13px;color:var(--ink)}
.institute{left:275px;top:150px;width:190px;text-align:center}
.institute-name{font-family:"Questrial",sans-serif;font-size:21px;color:#666;line-height:26px}
.institute-note{font-size:9px;color:var(--ink);margin-top:8px}
.photo{position:absolute}
.block{position:absolute;background:var(--red)}
.cover-title{left:0;width:490px;top:466px;text-align:center;color:var(--red);font-size:23px;letter-spacing:1.3px;font-weight:400}
.cover-sub{left:0;width:490px;top:497px;text-align:center;color:var(--red);font-size:16px;letter-spacing:1.2px;line-height:20px}
.year-tab{left:91px;top:670px;width:23px;height:24px;background:var(--red)}
.year-band{left:125px;top:670px;width:365px;height:24px;background:var(--red);color:#fff;font-size:15px;padding-left:17px;line-height:24px}

/* Inner page */
.inner{left:649px;top:54px;width:486px;height:688px}
.level-bar{left:77px;top:0;width:409px;height:26px;background:var(--red);color:#fff;font-family:"Montserrat",sans-serif;font-weight:600;font-size:17px;padding-left:16px;line-height:27px}
.course-head{left:9px;top:36px;font-family:"Montserrat",sans-serif;font-weight:700;font-size:9px;line-height:10px}
.label-red{font-family:"Montserrat",sans-serif;font-weight:600;color:var(--red);font-size:9.5px}
.testimonial{font-size:5.4px;line-height:6.2px;color:var(--soft);font-style:italic;width:200px}
.section-bar{height:17px;background:var(--red);color:#fff;font-family:"Montserrat",sans-serif;font-weight:600;font-size:10px;padding-left:4px;line-height:18px}
.body-text{font-size:6.5px;line-height:6.6px;color:var(--ink)}
.body-text p+p{margin-top:5px}
.body-text ul{list-style:none}
.body-text li::before{content:"• "}
.rule{height:1.5px;background:var(--red)}
.rule-grey{height:1px;background:#bbb}
.mini-head{font-family:"Montserrat",sans-serif;font-weight:700;font-size:6.2px}
.red-text{color:var(--red)}
.syllabus-bar{left:103px;top:327px;width:371px;height:16px;background:var(--red);color:#fff;font-family:"Montserrat",sans-serif;font-weight:500;font-size:7.5px;text-align:center;line-height:16px}
.day{font-family:"Montserrat",sans-serif;font-weight:700;font-size:6.2px;text-decoration:underline}
.lesson{width:112px}
.lesson-no{font-family:"Montserrat",sans-serif;font-weight:700;font-size:6.2px}
.lesson-topic{color:var(--red);font-size:5.8px;line-height:6.4px;margin-top:6px;text-transform:uppercase}
.lesson-points{font-size:6px;line-height:6.4px;margin-top:8px}
.profile-head{left:13px;top:553px;font-family:"Montserrat",sans-serif;font-weight:700;font-size:8px}
.profile-bio{left:103px;top:555px;width:255px;font-size:5.6px;line-height:6.3px;font-style:italic}
.contact{left:14px;top:636px;width:82px;font-size:4.8px;line-height:5.4px;font-style:italic}
</style>
</head>
<body>

<section class="page cover" aria-label="Front cover">
  <div class="abs partner">
    <p class="partner-name">Financial Advisers Guild<br>of Asia</p>
  </div>
  <div class="abs institute">
    <p class="institute-name">Brightvale Institute</p>
    <p class="institute-note">(division of Brightvale Holdings Pte Ltd)</p>
  </div>

  <div class="photo" role="img" aria-label="Photo of a financial planner advising a couple at a desk" style="left:34px;top:248px;width:171px;height:116px;background:linear-gradient(135deg,#d9c3a8,#8a6a52)"></div>
  <div class="photo" role="img" aria-label="Video conference screen with several professionals" style="left:213px;top:248px;width:191px;height:116px;background:linear-gradient(135deg,#8a3c5e,#5e2340)"></div>
  <div class="block" style="left:410px;top:248px;width:48px;height:116px"></div>
  <div class="block" style="left:34px;top:370px;width:87px;height:60px"></div>
  <div class="photo" role="img" aria-label="Photo of a seminar audience facing a presenter" style="left:125px;top:370px;width:88px;height:60px;background:linear-gradient(135deg,#c69a7c,#7b5643)"></div>
  <div class="photo" role="img" aria-label="Photo of a business handshake" style="left:218px;top:370px;width:84px;height:60px;background:linear-gradient(135deg,#9aa6b6,#3f4b5e)"></div>
  <div class="block" style="left:308px;top:370px;width:150px;height:60px"></div>

  <h1 class="abs cover-title">PRACTICAL FINANCIAL COUNSELLING</h1>
  <p class="abs cover-sub">A PRACTICAL APPROACH TO LEADING<br>OTHERS TO FINANCIAL WELLNESS</p>

  <div class="abs year-tab"></div>
  <div class="abs year-band">2014</div>
</section>

<section class="page inner" aria-label="Course details">
  <div class="abs level-bar">LEVEL 1</div>
  <p class="abs course-head">A PRACTICAL FIELD-TESTED COURSEWARE<br>FOR ADVANCED MARKET PLANNING</p>
  <p class="abs label-red" style="left:9px;top:61px">TESTIMONIALS</p>
  <p class="abs testimonial" style="left:9px;top:79px">"My team and I have benefited greatly from the generous sharing of ideas, concepts and strategies. The sessions have positively shaped the way we do our business and our results."<br>Grace Lee<br>Top Producer Circle 2010<br>Financial Services Associate Director<br>Pacific Crest Assurance</p>
  <p class="abs testimonial" style="left:246px;top:76px">"This a different way of raising an adviser's profile to be a trusted advisor who cares to educate, counsel and help people through a holistic approach."<br>Karen Ho<br>Senior Adviser<br>Financial Planning Director<br>Harbour Life Asia</p>

  <div class="abs section-bar" style="left:10px;top:129px;width:156px">OBJECTIVES</div>
  <div class="abs section-bar" style="left:243px;top:129px;width:155px">SYNOPSIS</div>

  <div class="abs body-text" style="left:12px;top:152px;width:222px">
    <ul>
      <li>Understand key differences between financial counseling and other forms of financial professionals and services</li>
      <li>Know about lending organisations, how they work and who governs them</li>
      <li>Understand the implications and consequences of financial distress including bankruptcy</li>
      <li>Develop the skills to help clients identify, clarify, explore, evaluate, decide and take appropriate actions in their financial situation</li>
      <li>Learn how to respond to common client questions and the language needed for successful communication</li>
      <li>Learn to work with other agencies to facilitate successful financial counselling</li>
      <li>Participate in role play to enhance effectiveness in engagement</li>
    </ul>
  </div>
  <div class="abs body-text" style="left:245px;top:152px;width:226px">
    <p>The field of financial counseling addresses one of the most urgent and growing needs of our time. The number and complexity of financial issues that ordinary people must face have grown dramatically.</p>
    <p>As people come under the stress of financial decisions (either for personal or business purposes), they would invariably seek out those who can provide the much needed assistance that is both objective and applied. They need to know the implications of their decisions and the consequences if things do not go well. Financial counseling is specifically help-oriented, personalized and focuses on leading them into financial wellness.</p>
    <p>Based on the immense experience and successful work of award-winning (Council for Financial Guidance Education) financial counsellor, Dr Harold M Reed, this course will equip you to serve a dire need in our society today.</p>
  </div>

  <div class="abs rule" style="left:11px;top:260px;width:464px"></div>

  <p class="abs mini-head" style="left:11px;top:272px">AWARD | CPD-Hours</p>
  <p class="abs body-text" style="left:11px;top:282px;width:165px">Participants who meet 75% class attendance are awarded a Certificate of Accomplishment. Financial services professionals get 18 CPD hours (50% knowledge, 50% skills) accreditation from Life Underwriters Council (LUC)</p>
  <p class="abs mini-head" style="left:183px;top:270px">DELIVERY METHODS</p>
  <p class="abs body-text" style="left:183px;top:282px;width:155px"><span class="red-text">The classes will be a combination of the following:</span><br>1. Classroom lecture-style<br>2. Discussion and case studies<br>3. Multiple role plays with feedback</p>
  <p class="abs mini-head" style="left:345px;top:270px">ASSESSMENT</p>
  <p class="abs body-text" style="left:345px;top:282px;width:130px">A closed book examination of 50 multiple-choice &amp; application questions on estate planning is conducted separately (passing mark 70%)</p>

  <div class="abs syllabus-bar">COURSE SYLLABUS | SCHEDULE 0930-1730 hours (2 days)</div>
  <p class="abs day" style="left:11px;top:339px">DAY ONE</p>

  <div class="abs lesson" style="left:11px;top:353px">
    <p class="lesson-no">Lesson 1:</p>
    <p class="lesson-topic">Financial Counseling Overview</p>
    <p class="lesson-points">-Myths and Truths about Financial Counseling<br>-Hallmarks of Financial Counseling<br>-Basic Approaches and Comparison<br>-Role Play in Explaining Financial Counselling</p>
  </div>
  <div class="abs lesson" style="left:127px;top:353px">
    <p class="lesson-no">Lesson 2:</p>
    <p class="lesson-topic">Regulating Lenders in Singapore</p>
    <p class="lesson-points">-Types of Legalized Lenders in Singapore<br>-Government Bodies that Regulated Lenders<br>-Non-Government Self-Regulating Bodies<br>-Laws that govern Lending in Singapore</p>
  </div>
  <div class="abs lesson" style="left:249px;top:353px">
    <p class="lesson-no">Lesson 3:</p>
    <p class="lesson-topic">The Business of Lending</p>
    <p class="lesson-points">-Common Types of Loans and their Implications<br>-Characteristics of Different Types of Loans<br>-Types of Interests, Penalties and Charges<br>-Role Play on Explaining Latest Rules</p>
  </div>
  <div class="abs lesson" style="left:366px;top:353px">
    <p class="lesson-no">Lesson 4:</p>
    <p class="lesson-topic">Credit Reporting</p>
    <p class="lesson-points">-The Role of Consumer Credit Reporting and its Implications<br>-Access to and Importance of Credit Information<br>-Maintaining a Good Credit Report<br>-Case Study of Significance of a Credit Report</p>
  </div>

  <p class="abs day" style="left:11px;top:434px">DAY TWO</p>
  <div class="abs lesson" style="left:11px;top:447px">
    <p class="lesson-no">Lesson 5:</p>
    <p class="lesson-topic">Borrowing – When Things Go Wrong</p>
    <p class="lesson-points">-Implications and Consequences of Defaults on Loans<br>-Impact of Bankruptcy and Role of the Insolvency Authority<br>-Rights, Duties and Responsibilities of Bankrupts (e.g. asset protection, discharge)<br>-Role Play on Explaining Journey to Bankruptcy</p>
  </div>
  <div class="abs lesson" style="left:127px;top:440px">
    <p class="lesson-no">Lesson 6:</p>
    <p class="lesson-topic">Legal and Illegal Assistance to Borrowers</p>
    <p class="lesson-points">-Comparing Public (e.g. Debt Relief Circle) and Private programs<br>-Dealing with Creditors (do's and don'ts)<br>-Illegal Money Lending Activities and their Consequences<br>-Role Play on Presenting Options and Dealing with Creditors</p>
  </div>
  <div class="abs lesson" style="left:249px;top:440px">
    <p class="lesson-no">Lesson 7:</p>
    <p class="lesson-topic">Rules of Engagement in Financial Counselling</p>
    <p class="lesson-points">• 5 Do's and Don'ts in Financial Counselling<br>• Basic &amp; Alternative Approaches to Financial Counselling<br>• Working with External Agencies to facilitate successful Financial Counselling<br>• Case Study of a Financial Counselling Situation</p>
  </div>
  <div class="abs lesson" style="left:366px;top:440px">
    <p class="lesson-no">Lesson 8:</p>
    <p class="lesson-topic">Processes and Tools in Financial Counselling</p>
    <p class="lesson-points">-6 Steps from Financial Distress to Financial Wellness<br>-Renewing the Mindset of a Counsellee (using the right language and tools)<br>-Creative Ideas in Reducing Expenses, Restructuring Debts, Reinventing Income Streams<br>-Exercises &amp; Role Plays on Real-life cases in Financial Counselling Applications</p>
  </div>

  <div class="abs rule-grey" style="left:11px;top:544px;width:464px"></div>

  <p class="abs profile-head">PROFILE OF TRAINER</p>
  <div class="abs" role="img" aria-label="Portrait photo of the course trainer" style="left:15px;top:566px;width:60px;height:65px;background:linear-gradient(160deg,#d8d0c8,#6f6a70)"></div>
  <p class="abs contact">CONTACT:<br>If you are interested in any of the given Courses and/or Certifications offered by the Guild, please contact us at:<br><br>Telephone: 6000 1234<br>Email: admin@faga.org.sg<br>Website: www.faga.org.sg</p>
  <p class="abs profile-bio">Daniel Tan FSWW is the principal trainer of Brightvale Institute (division of Brightvale Holdings Pte Ltd). With more than 20 years of experience as a financial service professional, he has been able to translate his skills and knowledge into transferable ideas through his practical training. He has designed and delivered highly-rated courses ranging from broad-based financial education &amp; counselling to specialized subjects like estate planning. His financial counselling programs have been extremely well-received by the civil service while his estate &amp; legacy planning training has reached more than 1500 financial services professionals through banks, insurers and advisory firms around the region. He is in constant demand for training and speaking engagements to the affluent market, civil service organisations and professional bodies. Daniel is a regular speaker at international adviser forums and congresses. He is an adjunct trainer &amp; course developer for the Eastbridge University's Financial Training Institute. He has also been interviewed by the regional business press and radio. He volunteers as a financial counsellor, is a member of the Guild's Alliance Team and a pioneer of a community financial counselling initiative by the financial services industry.</p>
  <p class="abs mini-head" style="left:370px;top:557px">DELIVERY METHODS</p>
  <p class="abs body-text" style="left:370px;top:570px;width:105px">The classes will be a combination of the following:<br>1. Classroom lecture-style<br>2. Discussion and case studies<br>3. Multiple role plays with feedback</p>
  <p class="abs mini-head" style="left:370px;top:615px">ASSESSMENT</p>
  <p class="abs body-text" style="left:370px;top:627px;width:105px">A closed book examination of 50 multiple-choice &amp; application questions on financial counselling is conducted separately (passing mark 70%)</p>
</section>

</body>
</html>
```